Re-Branding

I would like a new "brand" which will incorporate my new photo. I do title insurance in California for Harborline Deed Assurance Corp. Could be used on business cards or flyers.

Target Market(s)

Real Estate Professionals, Attorneys, Mortgage Companies and Banks.

Contact Information for Business Card

High Gloss

Requirements
Must have
• My photo, my logo and my contact information.
Nice to have
• background that is appealing to clients
Should not have
• home email address

```html
<!DOCTYPE html>
<html lang="en">
<head>
<meta charset="utf-8">
<title>Dana Whitfield – Business Card</title>
<link href="https://fonts.googleapis.com/css2?family=Cinzel:wght@600&family=Arimo:wght@400;700&display=swap" rel="stylesheet">
<style>
  :root {
    --backdrop: #d9dadc;
    --card: #ffffff;
    --brand-green: #1c7a45;
    --brand-navy: #1f2d5a;
    --photo-light: #eef0ee;
    --photo-mid: #2f9a5c;
    --photo-deep: #1a7a43;
  }
  * { box-sizing: border-box; margin: 0; padding: 0; }
  html, body { width: 1200px; height: 900px; overflow: hidden; }
  body {
    background: var(--backdrop);
    display: flex;
    align-items: center;
    justify-content: center;
    gap: 60px;
    font-family: "Arimo", Arial, sans-serif;
  }
  .card {
    width: 434px;
    height: 760px;
    background: var(--card);
    border-radius: 26px;
    box-shadow: 0 10px 30px rgba(0,0,0,0.18);
    overflow: hidden;
    position: relative;
    display: flex;
    flex-direction: column;
    align-items: center;
  }
  .card-header { text-align: center; padding-top: 70px; }
  .holder-name {
    font-family: "Cinzel", Georgia, serif;
    font-weight: 600;
    color: var(--brand-green);
    font-size: 31px;
    letter-spacing: 2px;
    line-height: 1;
  }
  .holder-title {
    color: var(--brand-navy);
    font-size: 17px;
    margin-top: 6px;
    letter-spacing: 0.5px;
  }
  .portrait {
    position: absolute;
    left: 40px; right: 0; bottom: 0;
    height: 560px;
    border-top-left-radius: 200px 160px;
    background: linear-gradient(180deg, var(--photo-light) 0%, var(--photo-mid) 45%, var(--photo-deep) 100%);
  }
  .contact-list {
    list-style: none;
    margin-top: 40px;
    display: flex;
    flex-direction: column;
    gap: 28px;
    align-items: center;
  }
  .contact-item {
    display: flex;
    flex-direction: column;
    align-items: center;
    gap: 12px;
    color: var(--brand-green);
    font-size: 20px;
    letter-spacing: 0.5px;
  }
  .contact-icon { width: 24px; height: 24px; display: block; }
  .company-mark {
    position: absolute;
    bottom: 60px;
    left: 0; right: 0;
    display: flex;
    align-items: center;
    justify-content: center;
    gap: 12px;
  }
  .company-dot {
    width: 40px; height: 40px;
    border-radius: 50%;
    background: var(--brand-navy);
    flex: none;
  }
  .company-name {
    color: var(--brand-navy);
    font-weight: 700;
    font-size: 18px;
    line-height: 1.2;
  }
</style>
</head>
<body>

  <section class="card card-front">
    <header class="card-header">
      <h1 class="holder-name">DANA WHITFIELD</h1>
      <p class="holder-title">Account Executive | Vice President</p>
    </header>
    <div class="portrait" role="img" aria-label="Portrait photo of the account executive in a green top"></div>
  </section>

  <section class="card card-back">
    <header class="card-header">
      <h2 class="holder-name">DANA WHITFIELD</h2>
      <p class="holder-title">Account Executive | Vice President</p>
    </header>

    <ul class="contact-list">
      <li class="contact-item">
        <svg class="contact-icon" viewBox="0 0 24 24" aria-hidden="true"><circle cx="12" cy="12" r="12" fill="#1f2d5a"/><path d="M8.5 6.5l2 2-1.2 1.6c.8 1.7 2 2.9 3.6 3.6l1.6-1.2 2 2-1.3 1.8c-4-.6-7.8-4.4-8.4-8.4z" fill="#fff"/></svg>
        <span>555-214-0938</span>
      </li>
      <li class="contact-item">
        <svg class="contact-icon" viewBox="0 0 24 24" aria-hidden="true"><circle cx="12" cy="12" r="12" fill="#1f2d5a"/><rect x="6.5" y="8" width="11" height="8" fill="none" stroke="#fff" stroke-width="1.4"/><path d="M6.5 8l5.5 4.5L17.5 8" fill="none" stroke="#fff" stroke-width="1.4"/></svg>
        <span>DWhitfield@hdac.com</span>
      </li>
      <li class="contact-item">
        <svg class="contact-icon" viewBox="0 0 24 24" aria-hidden="true"><circle cx="12" cy="12" r="12" fill="#1f2d5a"/><path d="M10.5 13.5l3-3M9.5 11l-1.5 1.5a2 2 0 0 0 3 3L12.5 14M14.5 13l1.5-1.5a2 2 0 0 0-3-3L11.5 10" fill="none" stroke="#fff" stroke-width="1.4" stroke-linecap="round"/></svg>
        <span>Dana.HarborlineIE.com</span>
      </li>
      <li class="contact-item">
        <svg class="contact-icon" viewBox="0 0 24 24" aria-hidden="true"><circle cx="12" cy="12" r="12" fill="#1f2d5a"/></svg>
        <span>harborline.page/DeedDesk/</span>
      </li>
      <li class="contact-item">
        <svg class="contact-icon" viewBox="0 0 24 24" aria-hidden="true"><circle cx="12" cy="12" r="12" fill="#1f2d5a"/></svg>
        <span>photos.harborline.page/dwhitfield/</span>
      </li>
    </ul>

    <div class="company-mark">
      <span class="company-dot" aria-hidden="true"></span>
      <span class="company-name">Harborline Deed<br>Assurance Corp.</span>
    </div>
  </section>

</body>
</html>
```